Brevane Advisory business card

Premium business card required
I have attached the brand as a powerpoint template but this can be made to look very up market, I have also attached my BIO for title reasons and to give you a feel for my skills
front of card
Darrel Voskuij
Managing Director Brevane Advisory
Retail, Customer-Led Experience, Transformation and Maximising Shareholder Return
Mobile +61(0)487395028
Email darrelbrevaneadvisory.example
back of card

BREVANE ADVISORY’ OFFERING

We transform customer environments to extract benefits while elevating service levels;
We release millions of dollars in self-funding through continuous improvement;
We see CX as a key differentiator, proactively guarding share from market disrupters;
We re-invent service and create front-end of the future.

```html
<!DOCTYPE html>
<html lang="en">
<head>
<meta charset="utf-8">
<title>Brevane Advisory business card</title>
<link rel="stylesheet" href="https://fonts.googleapis.com/css2?family=Open+Sans:wght@400;600;700;800&display=swap">
<style>
  :root {
    --bg: #2b2b2b;
    --gold-light: #ebe066;
    --gold: #d3bd3c;
    --gold-deep: #c4a62c;
    --gold-text: #d9b92e;
    --charcoal: #5a5a5a;
    --logo-grey: #575757;
    --white: #ffffff;
    --paper: #fbfbfb;
  }
  * { margin: 0; padding: 0; box-sizing: border-box; }
  html, body { width: 1200px; height: 900px; overflow: hidden; }
  body {
    background: var(--bg);
    font-family: "Open Sans", Arial, sans-serif;
    position: relative;
  }
  .card {
    position: absolute;
    left: 285px;
    width: 630px;
    height: 360px;
    overflow: hidden;
    box-shadow: 0 10px 30px rgba(0,0,0,.45);
  }
  /* Back of card */
  .card-back {
    top: 50px;
    background: linear-gradient(120deg, var(--gold-light) 0%, var(--gold) 55%, var(--gold-deep) 100%);
    color: var(--white);
    text-align: center;
  }
  .wordmark {
    display: flex;
    align-items: center;
    justify-content: center;
    gap: 14px;
    font-weight: 800;
    letter-spacing: .5px;
    white-space: nowrap;
  }
  .wordmark-dot {
    border-radius: 50%;
    flex: none;
  }
  .card-back .wordmark { margin-top: 72px; font-size: 46px; color: var(--white); }
  .card-back .wordmark-dot { width: 44px; height: 44px; background: var(--white); }
  .offering-title {
    margin-top: 30px;
    font-size: 15px;
    font-weight: 700;
  }
  .offering-list {
    list-style: none;
    margin-top: 8px;
    font-size: 12px;
    line-height: 1.45;
  }
  /* Front of card */
  .card-front {
    top: 490px;
    background: var(--paper);
  }
  .front-shapes { position: absolute; inset: 0; }
  .card-front .wordmark {
    position: absolute;
    left: 90px;
    top: 60px;
    font-size: 40px;
    color: var(--logo-grey);
    justify-content: flex-start;
  }
  .card-front .wordmark-dot { width: 38px; height: 38px; background: var(--logo-grey); }
  .holder {
    position: absolute;
    right: 26px;
    top: 207px;
    text-align: right;
    color: var(--white);
    font-size: 11px;
    line-height: 1.5;
    white-space: nowrap;
  }
  .holder-name {
    color: var(--gold-text);
    font-weight: 700;
    font-size: 14px;
    line-height: 1.3;
    text-transform: uppercase;
    margin-bottom: 1px;
  }
  .contacts {
    position: absolute;
    left: 26px;
    bottom: 14px;
    list-style: none;
    color: var(--white);
    font-size: 14px;
    line-height: 1.55;
    white-space: nowrap;
  }
  .contacts li { display: flex; align-items: center; gap: 10px; }
  .contacts svg { width: 13px; height: 13px; flex: none; }
</style>
</head>
<body>

<section class="card card-back" aria-label="Back of card">
  <div class="wordmark"><span>Brevane Advisory</span><span class="wordmark-dot"></span></div>
  <h2 class="offering-title">Brevane Advisory Offering</h2>
  <ul class="offering-list">
    <li>We transform customer environments to extract benefits while elevating service levels;</li>
    <li>We release millions of dollars in self-funding through continuous improvement;</li>
    <li>We see CX as a key differentiator, proactively guarding share from market disrupters;</li>
    <li>We re-invent service and create front-end of the future.</li>
  </ul>
</section>

<section class="card card-front" aria-label="Front of card">
  <svg class="front-shapes" viewBox="0 0 630 360" width="630" height="360" aria-hidden="true">
    <polygon points="0,262 262,262 296,196 630,196 630,360 0,360" fill="var(--charcoal)"/>
    <polygon points="0,246 258,246 253,255 0,255" fill="var(--gold)"/>
  </svg>

  <div class="wordmark"><span>Brevane Advisory</span><span class="wordmark-dot"></span></div>

  <div class="holder">
    <p class="holder-name">Darrel Voskuij</p>
    <p>Managing Director Brevane Advisory</p>
    <p>Retail, Customer-Led Experience</p>
    <p>Transformation &amp; Maximising Shareholder Return</p>
  </div>

  <ul class="contacts">
    <li>
      <svg viewBox="0 0 12 12"><rect x="3" y="0.5" width="6" height="11" rx="1" fill="none" stroke="var(--gold)" stroke-width="1.4"/></svg>
      +61(0)487395028
    </li>
    <li>
      <svg viewBox="0 0 12 12"><rect x="0.5" y="2.5" width="11" height="7" fill="var(--gold)"/><polyline points="0.5,2.5 6,7 11.5,2.5" fill="none" stroke="var(--charcoal)" stroke-width="1"/></svg>
      dv@darrelbrevaneadvisory.example
    </li>
    <li>
      <svg viewBox="0 0 12 12"><circle cx="6" cy="6" r="5.5" fill="var(--gold)"/><path d="M0.5 6h11M6 0.5c-2.5 3-2.5 8 0 11M6 0.5c2.5 3 2.5 8 0 11" fill="none" stroke="var(--charcoal)" stroke-width=".8"/></svg>
      darrelbrevaneadvisory.example
    </li>
  </ul>
</section>

</body>
</html>
```